Cobalt Margin Funds Bus card and Logo

I need a logo design and Bus card design. The fund focuses on evaluating and investing in minerals (sub-surface rights) and real estate.

Cobalt margin refers to a book of knowledge that each plebe gets when entering the Harwick Civic Academy (my alma mater)

Target Market(s)

Investors and financial advisors

Contact Information for Business Card

Simple - perhaps a logo with a theme on book of knowledge

Logo Text

Ex Scientia Imperium

Font styles to use
Serif
Sans Serif

Colors

Designer to choose colors to be used in the design.

Requirements
Must have
• memorable logo that is relatively simple

```html
<!DOCTYPE html>
<html lang="en">
<head>
<meta charset="utf-8">
<title>Cobalt Margin Funds — Business Card</title>
<link rel="stylesheet" href="https://fonts.googleapis.com/css2?family=Montserrat:wght@600&family=Roboto:wght@500&family=Work+Sans:wght@400&display=swap">
<style>
  :root {
    --backdrop: #242424;
    --paper: #ffffff;
    --navy: #153a69;
    --sky: #0aa5e6;
    --ink: #1d2f4f;
  }
  * { margin: 0; padding: 0; box-sizing: border-box; }
  html, body { width: 1200px; height: 900px; overflow: hidden; }
  body { background: var(--backdrop); position: relative; }

  .card {
    position: absolute;
    left: 261px;
    width: 656px;
    height: 358px;
    box-shadow: 0 4px 12px rgba(0,0,0,0.45);
  }
  .card--front { top: 69px; background: var(--paper); }
  .card--back  { top: 472px; background: var(--navy); }

  .brand {
    position: absolute;
    display: flex;
    flex-direction: column;
    align-items: center;
    font-family: "Montserrat", sans-serif;
    font-weight: 600;
    text-align: center;
    line-height: 1;
  }
  .brand__square { background: var(--sky); }
  .brand__name { letter-spacing: 0.02em; }

  .card--front .brand { left: 30px; width: 282px; top: 112px; color: var(--navy); }
  .card--front .brand__square { width: 42px; height: 42px; margin-bottom: 22px; }
  .card--front .brand__name { font-size: 27px; }
  .card--front .brand__sub { font-size: 18px; margin-top: 10px; letter-spacing: 0.06em; }

  .divider {
    position: absolute;
    left: 338px; top: 95px;
    width: 2px; height: 168px;
    background: var(--navy);
  }

  .contact {
    position: absolute;
    left: 374px; top: 90px;
    font-family: "Work Sans", sans-serif;
    color: var(--ink);
    font-size: 16px;
    line-height: 21px;
  }
  .contact__name {
    font-family: "Roboto", sans-serif;
    font-weight: 500;
    font-size: 32px;
    line-height: 36px;
    color: var(--sky);
    white-space: nowrap;
  }
  .contact__role { margin-bottom: 12px; }
  .contact__address { margin-bottom: 9px; }
  .contact__line { display: flex; align-items: center; gap: 8px; }
  .contact__line svg { width: 10px; height: 10px; flex: none; }

  .card--back .brand { left: 0; width: 656px; top: 92px; color: var(--paper); }
  .card--back .brand__square { width: 62px; height: 62px; margin-bottom: 28px; }
  .card--back .brand__name { font-size: 38px; }
  .card--back .brand__sub { font-size: 24px; margin-top: 10px; letter-spacing: 0.06em; }
</style>
</head>
<body>

  <section class="card card--front">
    <div class="brand">
      <div class="brand__square"></div>
      <div class="brand__name">COBALT MARGIN</div>
      <div class="brand__sub">FUNDS LLC</div>
    </div>

    <div class="divider"></div>

    <div class="contact">
      <div class="contact__name">DANIEL PORTER</div>
      <div class="contact__role">Director</div>
      <div class="contact__address">1180 Ridgeview Lane<br>Maple Grove, CA 95710</div>
      <div class="contact__line">
        <svg viewBox="0 0 10 10" aria-hidden="true"><path d="M2 1 L4 1 L4.5 3 L3.3 3.8 Q4.2 6 6.2 6.8 L7 5.6 L9 6 L9 8 Q5 9.5 2.5 6 Q1 3.5 2 1 Z" fill="var(--sky)"/></svg>
        <span>+330 5120-4476</span>
      </div>
      <div class="contact__line">
        <svg viewBox="0 0 10 10" aria-hidden="true"><rect x="0.7" y="2" width="8.6" height="6" fill="none" stroke="var(--sky)" stroke-width="1"/><path d="M0.7 2 L5 5.5 L9.3 2" fill="none" stroke="var(--sky)" stroke-width="1"/></svg>
        <span>info@cobaltmarginfunds.com</span>
      </div>
      <div class="contact__line">
        <svg viewBox="0 0 10 10" aria-hidden="true"><circle cx="5" cy="5" r="4.2" fill="none" stroke="var(--sky)" stroke-width="0.9"/><ellipse cx="5" cy="5" rx="1.8" ry="4.2" fill="none" stroke="var(--sky)" stroke-width="0.8"/><path d="M0.8 5 H9.2" stroke="var(--sky)" stroke-width="0.8"/></svg>
        <span>www.cobaltmarginfunds.com</span>
      </div>
    </div>
  </section>

  <section class="card card--back">
    <div class="brand">
      <div class="brand__square"></div>
      <div class="brand__name">COBALT MARGIN</div>
      <div class="brand__sub">FUNDS LLC</div>
    </div>
  </section>

</body>
</html>
```